homepage design , industry automation control image

we need a design , based on our Logo image.

we focus on selling of temprature sensor ,and parts.

but need concept or image on industry automation control

we need enviroment friendly concept.

Industry/Entity Type

Industry

Number of Pages Required

5+ page

Requirements
Must have
• we need a Cartoon Image of a Temperature sensor,
• attaching a Excel file with the sensor looking.
Nice to have
• Nature image, future concept

```html
<!DOCTYPE html>
<html lang="en">
<head>
<meta charset="utf-8">
<title>Kessler Messtechnik – Industry Automation</title>
<link rel="stylesheet" href="https://fonts.googleapis.com/css2?family=Jost:wght@300;400;500;600&display=swap">
<style>
:root{
  --green:#0a9a0a;
  --green-dark:#067a06;
  --green-light:#5fd12a;
  --text:#333333;
  --muted:#6b6b6b;
  --line:#e3e3e3;
  --white:#ffffff;
}
*{margin:0;padding:0;box-sizing:border-box}
html,body{width:1200px;height:2651px;overflow:hidden;background:var(--white)}
body{font-family:"Jost",sans-serif;color:var(--text);position:relative}
section,header,nav,footer{position:absolute;left:0;width:1200px}
.abs{position:absolute}
.center{text-align:center;left:0;width:1200px}

/* header */
.site-header{top:0;height:122px}
.brand{left:99px;top:34px;display:flex;align-items:center;gap:10px}
.brand-mark{width:50px;height:50px;background:var(--green)}
.brand-name{font-size:27px;font-weight:600;color:var(--green)}
.search{left:632px;top:44px;width:468px;height:37px;border:1px solid var(--line);display:flex;align-items:center;justify-content:space-between;padding:0 16px;font-size:15px;color:#8a8a8a}

/* nav */
.main-nav{top:122px;height:44px;background:linear-gradient(#19b019,#057a05)}
.main-nav ul{list-style:none;position:relative;height:44px}
.main-nav li{position:absolute;top:0;height:44px;line-height:44px;color:var(--white);font-size:17px;text-transform:uppercase}
.main-nav li.active{background:var(--green-light);width:132px;text-align:center;left:99px}

/* hero */
.hero{top:166px;height:525px}
.hero-photo{position:absolute;inset:0;background:linear-gradient(180deg,#8a97a6 0%,#6f7c72 30%,#3c5532 55%,#23364a 75%,#3d4f35 100%)}
.hero h1{top:150px;font-size:54px;font-weight:600;color:var(--white);letter-spacing:1px}
.hero p{top:222px;font-size:17px;color:var(--white)}
.btn-solid{background:var(--green);color:var(--white);font-weight:600;font-size:17px;text-align:center}
.hero .btn-solid{left:514px;top:281px;width:170px;height:41px;line-height:41px}
.dots{top:480px;left:0;width:1200px;display:flex;justify-content:center;gap:10px}
.dots span{width:14px;height:14px;border-radius:50%;background:var(--white)}
.dots span:first-child{background:transparent;border:2px solid var(--white)}

/* welcome */
.welcome{top:691px;height:634px}
.welcome h2{top:52px;font-size:40px;font-weight:300;color:#222}
.welcome h2 em,.about h2 em{font-style:normal;color:var(--green)}
.welcome .lead{top:112px;left:170px;width:860px;text-align:center;font-size:13.5px;line-height:28px;color:var(--muted)}
.divider{top:198px;left:318px;width:672px;height:1px;background:var(--line)}
.feature{top:240px;width:320px;text-align:center}
.feature .icon{width:148px;height:148px;margin:0 auto;border-radius:50%;background:var(--green);border:4px solid #0d7d0d;display:flex;align-items:center;justify-content:center}
.feature h3{margin-top:18px;font-size:21px;font-weight:400;color:#222}
.feature p{margin:6px auto 0;width:290px;font-size:13.5px;line-height:24px;color:var(--muted)}
.btn-outline{display:inline-block;border:2px solid var(--green);color:var(--green);font-size:16px;font-weight:500}
.feature .btn-outline{margin-top:26px;width:152px;height:44px;line-height:40px}

/* band */
.band{top:1325px;height:425px}
.band-photo{position:absolute;inset:0;background:linear-gradient(180deg,#3fbf3f 0%,#23a223 50%,#0d7a12 100%)}
.band h2{top:60px;font-size:42px;font-weight:400;color:var(--white)}
.band p{left:170px;width:860px;text-align:center;font-size:15px;line-height:29px;color:var(--white);font-weight:300}
.band .btn-line{left:454px;top:304px;width:294px;height:50px;line-height:48px;border:1px solid rgba(255,255,255,.8);color:var(--white);font-size:18px;text-align:center}

/* about */
.about{top:1750px;height:508px}
.about h2{top:60px;font-size:40px;font-weight:300;color:#222}
.about p{left:99px;width:530px;font-size:14.5px;line-height:26px;color:var(--muted)}
.about .btn-outline{left:99px;top:383px;width:235px;height:47px;line-height:43px;border-width:1px;text-align:center;font-size:17px}
.about-photo{left:663px;top:162px;width:440px;height:265px;border:1px solid #ddd;padding:8px;background:var(--white);box-shadow:0 1px 4px rgba(0,0,0,.15)}
.about-photo div{width:100%;height:100%;background:linear-gradient(180deg,#6d89a8 0%,#4d6c5c 45%,#3b5a35 100%)}

/* footer */
.site-footer{top:2258px;height:308px;background:linear-gradient(#0aa20a,#067206)}
.site-footer h4{font-size:22px;font-weight:400;color:var(--white)}
.col{top:56px}
.map{margin-top:14px;width:293px;height:163px;background:linear-gradient(135deg,#e8ece6,#d6dfd4);border:2px solid #dfe8df}
.contact p{margin-top:12px;font-size:15px;line-height:27px;color:#dff3df}
.contact .row{display:flex;align-items:center;gap:12px;color:var(--white);font-size:16px;line-height:30px}
.newsletter form{margin-top:14px;width:315px;height:44px;background:var(--white);display:flex;align-items:center;justify-content:space-between;padding:0 5px 0 12px;font-size:14px;color:#999}
.newsletter .subscribe{background:var(--green);color:var(--white);font-size:12px;font-weight:600;height:32px;line-height:32px;padding:0 15px}
.social{margin-top:18px;display:flex;gap:8px}
.social span{width:37px;height:37px;border-radius:50%;background:var(--white)}
.copyright{top:2566px;height:85px;line-height:85px;text-align:center;font-size:13.5px;color:#555}
</style>
</head>
<body>

<header class="site-header">
  <div class="abs brand"><span class="brand-mark"></span><span class="brand-name">Kessler Messtechnik</span></div>
  <div class="abs search"><span>Search entire here</span>
    <svg width="18" height="18" viewBox="0 0 18 18" fill="none" stroke="#bbb" stroke-width="1.6"><circle cx="7.5" cy="7.5" r="5.5"/><path d="M11.5 11.5l5 5"/></svg>
  </div>
</header>

<nav class="main-nav">
  <ul>
    <li class="active">Home</li>
    <li style="left:260px">About Us</li>
    <li style="left:411px">Services</li>
    <li style="left:554px">Features</li>
    <li style="left:701px">Pricing</li>
    <li style="left:838px">Blog</li>
    <li style="left:952px">Contact Us</li>
  </ul>
</nav>

<section class="hero">
  <div class="hero-photo" role="img" aria-label="Aerial view of a city skyline along a river with a bridge"></div>
  <h1 class="abs center">INDUSTRY AUTOMATION COMPANY</h1>
  <p class="abs center">Sed ut perspiciatis unde omnis iste natus error sit voluptatem accusantium doloremque</p>
  <div class="abs btn-solid">LEARN MORE</div>
  <div class="abs dots"><span></span><span></span><span></span><span></span></div>
</section>

<section class="welcome">
  <h2 class="abs center">Welcome to <em>Kessler Messtechnik</em></h2>
  <p class="abs lead">Sed ut perspiciatis unde omnis iste natus error sit voluptatem accusantium doloremque laudantium, totam rem aperiam, eaque ipsa quae ab illo inventore veritatis et quasi architecto beatae vitae dicta sunt explicabo.</p>
  <div class="abs divider"></div>

  <div class="abs feature" style="left:82px">
    <div class="icon">
      <svg width="70" height="80" viewBox="0 0 70 80" fill="none" stroke="#fff" stroke-width="4" stroke-linecap="round"><path d="M28 48V12a7 7 0 0 1 14 0v36a13 13 0 1 1-14 0z"/><circle cx="35" cy="59" r="5" fill="#fff"/><path d="M35 54V28M48 16h8M48 26h8M48 36h8"/></svg>
    </div>
    <h3>TEMPRATURE</h3>
    <p>Sed ut perspiciatis unde omnis iste natus error sit voluptatem accusantium.</p>
    <span class="btn-outline">READ MORE</span>
  </div>

  <div class="abs feature" style="left:441px">
    <div class="icon">
      <svg width="70" height="78" viewBox="0 0 70 78" fill="none" stroke="#fff" stroke-width="4" stroke-linecap="round"><circle cx="16" cy="12" r="7"/><circle cx="54" cy="12" r="7"/><circle cx="16" cy="66" r="7"/><circle cx="54" cy="66" r="7"/><path d="M16 19v6c0 14 38 14 38 28v6M54 19v6c0 14-38 14-38 28v6"/></svg>
    </div>
    <h3>FLOW</h3>
    <p>Sed ut perspiciatis unde omnis iste natus error sit voluptatem accusantium.</p>
    <span class="btn-outline">READ MORE</span>
  </div>

  <div class="abs feature" style="left:800px">
    <div class="icon">
      <svg width="76" height="76" viewBox="0 0 76 76" fill="none" stroke="#fff" stroke-width="4" stroke-linecap="round"><circle cx="38" cy="32" r="24"/><path d="M38 32l10-12M10 66h56M18 74h40M38 56v10"/><circle cx="38" cy="32" r="3" fill="#fff"/></svg>
    </div>
    <h3>PRESSURE CONTROL</h3>
    <p>Sed ut perspiciatis unde omnis iste natus error sit voluptatem accusantium.</p>
    <span class="btn-outline">READ MORE</span>
  </div>
</section>

<section class="band">
  <div class="band-photo" role="img" aria-label="Green-tinted industrial plant with chimneys and hills"></div>
  <h2 class="abs center">We are a Industry Automation Company</h2>
  <p class="abs" style="top:142px">But I must explain to you how all this mistaken idea of denouncing pleasure and praising pain was born and I will give you a complete account of the system, and expound the actual teachings of the great explorer of the truth</p>
  <p class="abs" style="top:220px">At vero eos et accusamus et iusto odio dignissimos ducimus qui blanditiis praesentium voluptatum deleniti atque corrupti quos dolores et quas molestias excepturi sint occaecati cupiditate non provident.</p>
  <div class="abs btn-line">LEARN MORE INFORMATION</div>
</section>

<section class="about">
  <h2 class="abs center">About <em>Us</em></h2>
  <p class="abs" style="top:156px">Nam libero tempore, cum soluta nobis est eligendi optio cumque nihil impedit quo minus id quod maxime placeat facere possimus, omnis voluptas assumenda est, omnis dolor repellendus</p>
  <p class="abs" style="top:256px">Temporibus autem quibusdam et aut officiis debitis aut rerum necessitatibus saepe eveniet ut et voluptates repudiandae sint et molestiae non recusandae. Itaque earum rerum hic tenetur a sapiente delectus.</p>
  <div class="abs btn-outline">MORE INFORMATION &nbsp;›</div>
  <div class="abs about-photo"><div role="img" aria-label="Office tower rising above a green wooded landscape"></div></div>
</section>

<footer class="site-footer">
  <div class="abs col" style="left:99px">
    <h4>Our Map</h4>
    <div class="map" role="img" aria-label="Street map showing the company location"></div>
  </div>
  <div class="abs col contact" style="left:477px">
    <h4>Contact Us</h4>
    <p>Kessler Messtechnik, Street Name,<br>City Address, Country, Pin Code.</p>
    <div class="row"><svg width="16" height="16" viewBox="0 0 16 16" fill="#fff"><path d="M3 1l3 3-2 2c1 2 3 4 6 6l2-2 3 3-2 2C7 15 1 9 1 3z"/></svg>+1-555-010-2400</div>
    <div class="row"><svg width="16" height="13" viewBox="0 0 16 13" fill="#fff"><path d="M0 0h16v2L8 7 0 2zM0 4l8 5 8-5v9H0z"/></svg>info@kessler-mess.com</div>
  </div>
  <div class="abs col newsletter" style="left:788px">
    <h4>Join Newsletters</h4>
    <form><span>EMAIL ADDRESS</span><span class="subscribe">SUBSCRIBE</span></form>
    <div class="social"><span></span><span></span><span></span><span></span><span></span></div>
  </div>
</footer>

<div class="abs copyright" style="left:0;width:1200px">© 2017 Kessler Messtechnik. &nbsp;All right reserved. &nbsp;Term of Use</div>

</body>
</html>
```